International Development Cooperation Consultant needs a business card design

I need a business card design for myself as a way to present and introduce to wide range of organisations: international organisations, NGOs, governments, universities....
I am a consultant working in the field of governance, civil society and public sector. I carry out studies and provide advice for development agencies as well as think tanks on different topics such as civil society organisations in developing countries, corruption, climate change, monitoring and evaluation. I also provide technical assistance to governments in developing countries... These studies should help for example NGOs to play a better role in poor countries or where they are threatened, or improved the impact of aid in developing countries. Technical capacity should strengthen the organisation and empower the public civl servants in those countries. I would like to see designs that give a fresh, young, positive, alternative but at the same time serious impression. That reflects change, connecting people, the world, knowledge, multi-culturality... Most of people I have worked with say that 'I make things happen' !
Industry/Entity Type
Business
Contact Information for Business Card
Laia Corbera Vidal
International Development Consultant
Governance Expert
E-mail: laiacorbera@mailnest-example.com
Phone: +34655203817

```html
<!DOCTYPE html>
<html lang="en">
<head>
<meta charset="utf-8">
<title>Laia Corbera Vidal – Business Card</title>
<link href="https://fonts.googleapis.com/css2?family=Roboto+Condensed:wght@400;700&family=Arimo:wght@700&display=swap" rel="stylesheet">
<style>
  :root {
    --backdrop: #ecebe8;
    --card-green: #02522b;
    --card-white: #ffffff;
    --ink: #111111;
    --ink-soft: #2b2b2b;
    --globe-sea: #a9c3e3;
    --globe-land: #cfe0bf;
    --shadow: rgba(0, 0, 0, 0.18);
  }
  * { margin: 0; padding: 0; box-sizing: border-box; }
  html, body {
    width: 1200px;
    height: 800px;
    overflow: hidden;
    background: var(--backdrop);
  }
  .stage {
    position: relative;
    width: 1200px;
    height: 800px;
  }
  .card {
    position: absolute;
    top: 227px;
    width: 520px;
    height: 346px;
    box-shadow: 0 6px 18px var(--shadow);
    overflow: hidden;
  }
  .card-front {
    left: 60px;
    background: var(--card-green);
  }
  .card-back {
    left: 620px;
    background: var(--card-white);
  }
  .person-name {
    font-family: "Roboto Condensed", "Arial Narrow", sans-serif;
    font-weight: 700;
    font-size: 24px;
    line-height: 28px;
    color: var(--ink);
    white-space: nowrap;
  }
  .person-role {
    font-family: "Roboto Condensed", "Arial Narrow", sans-serif;
    font-weight: 400;
    font-size: 15px;
    line-height: 19px;
    color: var(--ink-soft);
    white-space: nowrap;
  }
  .front-band {
    position: absolute;
    left: 0;
    top: 136px;
    width: 480px;
    height: 66px;
    background: var(--card-white);
    border-radius: 0 33px 33px 0;
    display: flex;
    flex-direction: column;
    justify-content: center;
    padding-left: 22px;
  }
  .globe {
    position: absolute;
    left: 130px;
    top: 36px;
    width: 260px;
    height: 260px;
  }
  .back-heading {
    position: absolute;
    left: 0;
    right: 0;
    top: 92px;
    text-align: center;
  }
  .contact {
    position: absolute;
    left: 0;
    right: 0;
    top: 240px;
    text-align: center;
    font-family: "Arimo", Arial, sans-serif;
    font-weight: 700;
    font-size: 20px;
    line-height: 31px;
    color: var(--ink);
  }
</style>
</head>
<body>
<main class="stage">
  <section class="card card-front">
    <div class="front-band">
      <p class="person-name">Laia Corbera Vidal</p>
      <p class="person-role">International Development Consultant · Governance Expert</p>
    </div>
  </section>

  <section class="card card-back">
    <svg class="globe" viewBox="0 0 260 260" role="img" aria-label="Faint globe encircled by a ring of children holding hands">
      <defs>
        <radialGradient id="globeFill" cx="50%" cy="50%" r="50%">
          <stop offset="0%" stop-color="var(--globe-land)" stop-opacity="0.75"/>
          <stop offset="70%" stop-color="var(--globe-sea)" stop-opacity="0.55"/>
          <stop offset="100%" stop-color="var(--globe-land)" stop-opacity="0"/>
        </radialGradient>
      </defs>
      <circle cx="130" cy="130" r="130" fill="url(#globeFill)"/>
    </svg>
    <div class="back-heading">
      <p class="person-name">Laia Corbera Vidal</p>
      <p class="person-role">International Development Consultant</p>
      <p class="person-role">Governance Expert</p>
    </div>
    <div class="contact">
      <p>Phone: +34655203817</p>
      <p>Email: laiacorbera@mailnest-example.com</p>
    </div>
  </section>
</main>
</body>
</html>
```